Gourmet Restaurant take out menu

We need a take out menu design that is trendy for a casual upscale Italian restaurant with a vast menu. This menu must be able to be 4 color and reproducible in large quantities to be bulked mailed or inserted into a daily paper. It must also maintain a theme that can be crossed over to our in house dining menu and specials menu.
OUR WEBSITE:
www.velmorabistrohouse.example
For the content, go to the Menu section of our website. We are interested in the design scheme and a template to use.
Target Market(s)
families, sinle individuals seeking take out meals and delivery
Industry/Entity Type
Restaurant

```html
<!DOCTYPE html>
<html lang="en">
<head>
<meta charset="utf-8">
<title>Menu Template – Cover and Inner Spread</title>
<link href="https://fonts.googleapis.com/css2?family=Cinzel:wght@400;700&family=Playfair+Display:wght@700&family=Prata&display=swap" rel="stylesheet">
<style>
  :root {
    --backdrop: #e6e6e6;
    --ink-black: #050505;
    --wood-dark: #161616;
    --wood-mid: #262626;
    --gold-dark: #9c7326;
    --gold: #d4a43c;
    --parchment-light: #f3dca3;
    --parchment: #e4b96a;
    --parchment-deep: #c98f3e;
    --rope: #8a5d2e;
    --rope-light: #c8995c;
    --rule: #a8622a;
    --rule-thin: #b87a45;
    --panel: rgba(160, 95, 40, 0.28);
    --white: #ffffff;
    --silver: #d9d9d9;
  }
  * { box-sizing: border-box; margin: 0; padding: 0; }
  html, body { width: 766px; height: 1200px; overflow: hidden; background: var(--backdrop); }
  .canvas { position: relative; width: 766px; height: 1200px; }

  .spine { position: absolute; background: var(--ink-black); }
  .spine--cover { left: 560px; top: 82px; width: 76px; height: 452px; border-radius: 0 14px 14px 0; }
  .spine--inner { left: 132px; top: 627px; width: 70px; height: 452px; border-radius: 14px 0 0 14px; }

  .page { position: absolute; width: 226px; height: 452px; overflow: hidden; }
  .page + .page { border-left: 1px solid rgba(60, 35, 10, 0.35); }
  .page svg.page-art { position: absolute; inset: 0; width: 226px; height: 452px; }

  .parchment {
    position: absolute; inset: 0;
    background:
      radial-gradient(ellipse at 50% 40%, var(--parchment-light) 0%, rgba(243,220,163,0) 60%),
      linear-gradient(180deg, var(--parchment) 0%, var(--parchment-light) 45%, var(--parchment) 80%, var(--parchment-deep) 100%);
  }
  .rope-border {
    position: absolute; left: 0; right: 0; bottom: 0; height: 92px;
    background: linear-gradient(180deg, rgba(138,93,46,0) 0%, var(--rope-light) 35%, var(--rope) 75%, #5e3c1b 100%);
  }

  /* Cover */
  .cover-left { left: 131px; top: 82px; }
  .cover-right { left: 357px; top: 82px; }
  .cover-mark { position: absolute; left: 0; width: 240px; top: 62px; text-align: center; }
  .cover-mark .ornament {
    position: absolute; left: 72px; top: 4px; width: 96px; height: 40px;
    background: radial-gradient(ellipse, rgba(200,200,200,0.45), rgba(200,200,200,0) 70%);
  }
  .cover-mark .utensils { position: relative; display: block; margin: 0 auto; width: 20px; height: 44px; }
  .cover-title {
    font-family: "Playfair Display", serif; font-weight: 700; font-size: 34px;
    letter-spacing: 0; color: var(--silver); line-height: 1; margin-top: 2px;
    background: linear-gradient(180deg, #ffffff 20%, #9a9a9a 100%);
    -webkit-background-clip: text; background-clip: text; -webkit-text-fill-color: transparent;
  }
  .cover-mark .swash {
    width: 56px; height: 14px; margin: 6px auto 0;
    background: radial-gradient(ellipse, rgba(180,180,180,0.5), rgba(180,180,180,0) 70%);
  }
  .tagline { position: absolute; left: 0; right: 0; top: 86px; text-align: center; color: var(--white); font-family: "Cinzel", serif; }
  .tagline-top { display: flex; align-items: center; justify-content: center; gap: 6px; font-size: 17px; line-height: 1; }
  .tagline-top::before, .tagline-top::after { content: ""; width: 68px; height: 2px; background: var(--white); }
  .tagline-bottom { font-size: 16px; margin-top: 8px; letter-spacing: 0.5px; }

  /* Inner spread */
  .inner-left { left: 182px; top: 627px; }
  .inner-right { left: 408px; top: 627px; }
  .section-head { position: absolute; text-align: center; font-family: "Prata", serif; font-size: 13px; color: #1a1209; }
  .section-head .label { display: inline-block; border-bottom: 1px solid #1a1209; padding: 0 4px 1px; line-height: 1.1; }
  .section-head svg { display: block; margin: 0 auto 3px; }
  .section-head--food { left: 8px; width: 84px; top: 28px; }
  .section-head--drink { left: 126px; width: 86px; top: 40px; }

  .photo { position: absolute; top: 0; height: 112px; }
  .photo--pasta {
    left: 74px; width: 152px; border-radius: 40px 0 0 60px;
    background: radial-gradient(ellipse at 55% 40%, #b8331c 0%, #c9541f 30%, #e8b640 58%, #f3ece0 80%);
  }
  .photo--drinks {
    left: 0; width: 134px;
    background: linear-gradient(90deg, #5a1420 0%, #a3203a 30%, #7a2a2a 65%, rgba(228,185,106,0) 100%);
  }

  .menu-panel { position: absolute; top: 128px; height: 265px; background: var(--panel); }
  .inner-left .menu-panel { left: 16px; right: 0; }
  .inner-right .menu-panel { left: 0; right: 17px; }
  .menu-rows { position: absolute; top: 12px; height: 252px; }
  .rows-items {
    background:
      repeating-linear-gradient(180deg, var(--rule) 0 3px, transparent 3px 18px),
      repeating-linear-gradient(180deg, transparent 0 8px, var(--rule-thin) 8px 9px, transparent 9px 18px);
    background-size: 74px 18px, 100% 18px;
    background-repeat: repeat-y;
  }
  .rows-prices { background: repeating-linear-gradient(180deg, var(--rule) 0 3px, transparent 3px 18px); }
  .inner-left .rows-items { left: 13px; width: 101px; }
  .inner-left .rows-prices { left: 153px; width: 45px; }
  .inner-right .rows-prices { left: 12px; width: 46px; }
  .inner-right .rows-items { left: 97px; width: 100px; background-position: 26px 0, 0 0; }
</style>
</head>
<body>
<main class="canvas">

  <!-- Cover spread -->
  <div class="spine spine--cover"></div>

  <section class="page cover-left">
    <div class="parchment"></div>
    <div class="rope-border" role="img" aria-label="Coiled rope photograph along the bottom edge"></div>
    <svg class="page-art" viewBox="0 0 226 452" aria-hidden="true">
      <defs>
        <linearGradient id="goldBand" x1="0" x2="1">
          <stop offset="0" stop-color="var(--gold-dark)"/>
          <stop offset="0.6" stop-color="var(--gold)"/>
          <stop offset="1" stop-color="var(--gold-dark)"/>
        </linearGradient>
        <linearGradient id="wood" x1="0" x2="1">
          <stop offset="0" stop-color="var(--wood-dark)"/>
          <stop offset="0.5" stop-color="var(--wood-mid)"/>
          <stop offset="1" stop-color="var(--wood-dark)"/>
        </linearGradient>
      </defs>
      <path d="M0,0 H226 V252 Q113,216 0,252 Z" fill="url(#goldBand)"/>
      <path d="M0,250 Q113,214 226,250 L226,268 Q113,232 0,268 Z" fill="var(--ink-black)"/>
      <path d="M0,0 H226 V188 Q113,246 0,191 Z" fill="var(--ink-black)"/>
      <path d="M0,0 H226 V176 Q113,230 0,179 Z" fill="url(#wood)"/>
    </svg>
    <div class="cover-mark">
      <div class="ornament" role="img" aria-label="Silver leaf flourish ornament"></div>
      <svg class="utensils" viewBox="0 0 20 44" aria-hidden="true">
        <ellipse cx="5" cy="7" rx="4" ry="6" fill="var(--white)"/>
        <rect x="4" y="12" width="2" height="32" fill="var(--white)"/>
        <rect x="11" y="0" width="1.2" height="10" fill="var(--white)"/>
        <rect x="13.6" y="0" width="1.2" height="10" fill="var(--white)"/>
        <rect x="16.2" y="0" width="1.2" height="10" fill="var(--white)"/>
        <path d="M11,9 H17.4 Q17.4,14 15,15 V44 H13.4 V15 Q11,14 11,9 Z" fill="var(--white)"/>
      </svg>
      <h1 class="cover-title">MENU</h1>
      <div class="swash" role="img" aria-label="Silver swash ornament"></div>
    </div>
  </section>

  <section class="page cover-right">
    <div class="parchment"></div>
    <div class="rope-border" role="img" aria-label="Coiled rope photograph along the bottom edge"></div>
    <svg class="page-art" viewBox="0 0 226 452" aria-hidden="true">
      <path d="M0,0 H226 V252 Q113,216 0,252 Z" fill="url(#goldBand)"/>
      <path d="M0,250 Q113,214 226,250 L226,268 Q113,232 0,268 Z" fill="var(--ink-black)"/>
      <path d="M0,0 H226 V188 Q113,246 0,191 Z" fill="var(--ink-black)"/>
      <path d="M0,0 H226 V176 Q113,230 0,179 Z" fill="url(#wood)"/>
    </svg>
    <div class="tagline">
      <div class="tagline-top">YOUR</div>
      <div class="tagline-bottom">TAG LINE HERE</div>
    </div>
  </section>

  <!-- Inner spread -->
  <div class="spine spine--inner"></div>

  <section class="page inner-left">
    <div class="parchment"></div>
    <div class="rope-border" role="img" aria-label="Coiled rope photograph along the bottom edge"></div>
    <div class="photo photo--pasta" role="img" aria-label="Photograph of spaghetti with tomato meat sauce and basil"></div>
    <div class="section-head section-head--food">
      <svg width="14" height="34" viewBox="0 0 14 34" aria-hidden="true">
        <ellipse cx="3.5" cy="5" rx="3" ry="5" fill="#111"/>
        <rect x="2.6" y="9" width="1.8" height="25" fill="#111"/>
        <rect x="8" y="0" width="1" height="8" fill="#111"/>
        <rect x="10" y="0" width="1" height="8" fill="#111"/>
        <rect x="12" y="0" width="1" height="8" fill="#111"/>
        <path d="M8,7 H13 Q13,11 11.3,12 V34 H9.7 V12 Q8,11 8,7 Z" fill="#111"/>
      </svg>
      <span class="label">Food Menu</span>
    </div>
    <div class="menu-panel">
      <div class="menu-rows rows-items"></div>
      <div class="menu-rows rows-prices"></div>
    </div>
  </section>

  <section class="page inner-right">
    <div class="parchment"></div>
    <div class="rope-border" role="img" aria-label="Coiled rope photograph along the bottom edge"></div>
    <div class="photo photo--drinks" role="img" aria-label="Photograph of two glasses of red fruit punch with citrus slices"></div>
    <div class="section-head section-head--drink">
      <svg width="14" height="34" viewBox="0 0 14 34" aria-hidden="true">
        <path d="M1,0 H13 Q14,12 7.8,15 V31 H11 V33 H3 V31 H6.2 V15 Q0,12 1,0 Z" fill="#111"/>
      </svg>
      <span class="label">Drink Menu</span>
    </div>
    <div class="menu-panel">
      <div class="menu-rows rows-prices"></div>
      <div class="menu-rows rows-items"></div>
    </div>
  </section>

</main>
</body>
</html>
```